Business Card Design

Consultant ot credit unions that operate a property and casualty insurance agency

Industry/Entity Type

Insurance

Contact Information for Business Card

Dorian Velker
Credit Union Insurance Agency Consultant
dorianvelker@mailvoro.com
562 318-4092
914 Tamsin Court
Long Beach, CA 90813

```html
<!DOCTYPE html>
<html lang="en">
<head>
<meta charset="utf-8">
<title>Dorian Velker – Business Card</title>
<link rel="stylesheet" href="https://fonts.googleapis.com/css2?family=Play:wght@400;700&family=Oswald:wght@500&family=Michroma&display=swap">
<style>
  :root {
    --stage: #8c8c8c;
    --card-white: #ffffff;
    --card-black: #1f2122;
    --soft-gray: #dcdcdc;
    --orange: #f4931e;
    --orange-deep: #e8761c;
    --ink: #1b1b1b;
  }
  html, body {
    margin: 0;
    width: 1200px;
    height: 900px;
    overflow: hidden;
    background: var(--stage);
  }
  .card {
    position: absolute;
    left: 100px;
    top: 150px;
    width: 1000px;
    height: 600px;
    border-radius: 34px;
    overflow: hidden;
    background: var(--card-white);
    box-shadow: 0 18px 40px rgba(0,0,0,0.35);
  }
  .card-art {
    position: absolute;
    inset: 0;
  }
  .brand-square {
    position: absolute;
    left: 52px;
    top: 52px;
    width: 176px;
    height: 176px;
    border-radius: 22px;
    background: var(--orange);
  }
  .name {
    position: absolute;
    left: 268px;
    top: 52px;
    margin: 0;
    font-family: "Play", sans-serif;
    font-weight: 700;
    font-size: 88px;
    line-height: 1;
    color: var(--orange);
    letter-spacing: -1px;
  }
  .role {
    position: absolute;
    left: 270px;
    top: 158px;
    margin: 0;
    font-family: "Oswald", sans-serif;
    font-weight: 500;
    font-size: 32px;
    line-height: 1;
    color: var(--ink);
    letter-spacing: 0.3px;
  }
  .contact {
    position: absolute;
    right: 40px;
    top: 330px;
    margin: 0;
    text-align: right;
    font-family: "Play", sans-serif;
    font-style: normal;
  }
  .contact .phone {
    display: block;
    font-size: 36px;
    color: var(--orange);
    line-height: 1.2;
  }
  .contact .email,
  .contact .address {
    display: block;
    font-size: 27px;
    color: var(--card-white);
    line-height: 1.35;
    letter-spacing: 0.5px;
  }
  .tagline {
    position: absolute;
    left: 60px;
    right: 40px;
    bottom: 42px;
    margin: 0;
    display: flex;
    justify-content: space-between;
    font-family: "Michroma", sans-serif;
    font-size: 18px;
    color: var(--orange);
    text-transform: uppercase;
  }
</style>
</head>
<body>
  <section class="card" aria-label="Business card">
    <svg class="card-art" viewBox="0 0 1000 600" width="1000" height="600" aria-hidden="true">
      <path class="gray-band" d="M0,350 C250,360 450,330 600,295 L1000,175 L1000,600 L0,600 Z" fill="var(--soft-gray)"/>
      <path class="orange-swoosh" d="M540,335 C720,275 900,175 1000,70 L1000,118 C880,205 720,285 540,335 Z" fill="var(--orange-deep)"/>
      <path class="black-field" d="M0,490 C300,420 650,330 1000,185 L1000,600 L0,600 Z" fill="var(--card-black)"/>
    </svg>

    <div class="brand-square" aria-hidden="true"></div>
    <h1 class="name">Dorian Velker</h1>
    <p class="role">CREDIT UNION INSURANCE AGENCY CONSULTANT</p>

    <address class="contact">
      <span class="phone">562 318-4092</span>
      <span class="email">dorianvelker@mailvoro.com</span>
      <span class="address">914 Tamsin Court Long Beach, CA 90813</span>
    </address>

    <p class="tagline" aria-label="Focused on you">
      <span>F</span><span>O</span><span>C</span><span>U</span><span>S</span><span>E</span><span>D</span>
      <span>&nbsp;</span>
      <span>O</span><span>N</span>
      <span>&nbsp;</span>
      <span>Y</span><span>O</span><span>U</span>
    </p>
  </section>
</body>
</html>
```